Business Card for Restaurant Vendal

This project consist of creating 2 design for business card of restaurant named Vendal.

The attached specs below are 'ONLY SUGGESTION' if you have others ideas. You are welcome to post it.

1) Restaurant Card

Adresse:
2784 Côte du Pinard Vert
Montréal (Qc) H4K 3T8

Website:
www.ven-dal.ca

Phone:
438-719-2046

2) Employee Card

Name: Lorna Pik
Title: Owner

Address:
2784 Côte du Pinard Vert
Montréal (Qc) H4K 3T8

Email:lorna@ven-dal.ca
Phone Number:438-719-2046
Cellphone Number:514-830-4162

 The attached specs are 'ONLY SUGGESTION' if you have others ideas.  You are welcome to post it.

Industry/Entity Type

Restaurant

Requirements
Must have
• UV Card Spot

To print Spot UV business cards you would have to submit 2 files for each side. The first file "base" would be your regular design file as it would have been in any other case. The 2nd file "UV mask" is a black/white file. The BLACK color will indicate the areas that will be covered with the UV high gloss finish. To upload the files, please combine front design and front mask file in one P
Nice to have
• 1) The font of the logo should be ink effect
2) black background with wallpaper effect
3) The specs below are 'ONLY SUGGESTION' if you have others ideas. You are welcome to post it.

```html
<!DOCTYPE html>
<html lang="fr">
<head>
<meta charset="utf-8">
<title>Vendal – Cartes d'affaires</title>
<link href="https://fonts.googleapis.com/css2?family=Open+Sans:wght@400;700&family=Noto+Sans+JP:wght@400&display=swap" rel="stylesheet">
<style>
  :root {
    --page-bg: #efeff0;
    --card-dark: #262424;
    --card-dark-2: #1d1c1c;
    --ink-white: #f4f2ef;
    --accent-red: #d0161b;
    --lantern-tone: #3a3737;
  }
  * { margin: 0; padding: 0; box-sizing: border-box; }
  html, body { width: 1031px; height: 1200px; overflow: hidden; }
  body {
    background: var(--page-bg);
    font-family: "Open Sans", sans-serif;
    position: relative;
  }
  .card {
    position: absolute;
    left: 32px;
    width: 967px;
    height: 554px;
    background: linear-gradient(90deg, var(--card-dark), var(--card-dark-2) 50%, var(--card-dark));
    overflow: hidden;
  }
  .card--front { top: 37px; }
  .card--back { top: 608px; }

  .lantern-area {
    position: absolute;
    width: 246px;
    height: 290px;
    background: var(--lantern-tone);
    border-radius: 6px;
  }
  .card--front .lantern-area { left: 0; top: 133px; }
  .card--back .lantern-area { left: 720px; top: 132px; }

  .brand {
    position: absolute;
    left: 432px;
    top: 196px;
    display: flex;
    align-items: center;
    gap: 14px;
  }
  .brand__name {
    font-weight: 700;
    font-size: 112px;
    line-height: 1;
    color: var(--ink-white);
    letter-spacing: 1px;
  }
  .brand__dot {
    width: 22px;
    height: 22px;
    border-radius: 50%;
    background: var(--accent-red);
    align-self: flex-start;
    margin-top: 6px;
  }
  .tagline {
    position: absolute;
    left: 460px;
    top: 340px;
    font-size: 17.5px;
    color: var(--ink-white);
    white-space: nowrap;
  }
  .tagline__sep { color: var(--accent-red); margin: 0 4px; }
  .tagline__jp { color: var(--accent-red); font-family: "Noto Sans JP", sans-serif; }

  .contact {
    position: absolute;
    right: 428px;
    top: 162px;
    text-align: right;
    color: var(--ink-white);
    font-size: 31px;
    line-height: 39px;
    font-style: normal;
  }
  .contact__block + .contact__block { margin-top: 38px; }
</style>
</head>
<body>
  <section class="card card--front">
    <div class="lantern-area" role="img" aria-label="Illustration décorative d'une lanterne en papier blanche"></div>
    <div class="brand">
      <span class="brand__name">Vendal</span>
      <span class="brand__dot"></span>
    </div>
    <p class="tagline">Resto-Bar Japonais<span class="tagline__sep">·</span>Izakaya<span class="tagline__sep">·</span><span class="tagline__jp">居酒屋</span></p>
  </section>

  <section class="card card--back">
    <address class="contact">
      <div class="contact__block">2784 Côte du Pinard Vert<br>Montréal (Qc) H4K 3T8</div>
      <div class="contact__block">www.ven-dal.ca</div>
      <div class="contact__block">438-719-2046</div>
    </address>
    <div class="lantern-area" role="img" aria-label="Illustration décorative d'une lanterne en papier blanche"></div>
  </section>
</body>
</html>
```